Health Supplement Series for 60 tablets of pure Tamrel Vine Kernel powder

We need a packaging design theme for a health supplement for international consumers. Our initial product is called 'Tamrel Vine Kernel'. It is for general health and is particularly effective for diabetic symptoms.
We would like to see designs that are clean and fresh.
It should give the impression of professional, premium pharmaceutical grade products.
Our company logo is attached below.

Target Market(s)

International

Industry/Entity Type

Health And Wellness

Font styles to use
Serif
Sans Serif

Requirements
Must have
• Bottle and box packaging required.
• 1st product is bottle of 60 tablets of 0.5gm each.
Should not have
• Seals and other "must buy" "guaranteed" etc

```html
<!DOCTYPE html>
<html lang="en">
<head>
<meta charset="utf-8">
<title>Tamrel Vine Kernel – Label</title>
<link rel="stylesheet" href="https://fonts.googleapis.com/css2?family=Open+Sans:wght@400;700;800&display=swap">
<style>
  :root {
    --backdrop: #efefef;
    --label-white: #ffffff;
    --brand-green: #5a9e2c;
    --vine-green: #5f9a3a;
    --vine-light: #a9cf8a;
    --title-brown-dark: #5a2210;
    --title-brown-light: #8a4a30;
    --band-brown: #6b2a12;
    --band-brown-light: #a3532c;
    --seed-dark: #5c2d14;
    --seed-light: #c0713e;
    --body-grey: #555555;
  }
  * { margin: 0; padding: 0; box-sizing: border-box; }
  html, body {
    width: 1158px; height: 1200px; overflow: hidden;
    background: var(--backdrop);
    font-family: "Open Sans", sans-serif;
  }
  .label {
    position: absolute; left: 115px; top: 20px;
    width: 928px; height: 1160px;
    background: var(--label-white);
    overflow: hidden;
    box-shadow: 0 4px 18px rgba(0,0,0,0.08);
  }
  .label__bands { position: absolute; inset: 0; width: 100%; height: 100%; }
  .vine {
    position: absolute;
    background: linear-gradient(180deg, var(--vine-green), var(--vine-light) 70%, rgba(169,207,138,0));
    border-radius: 40px;
    opacity: 0.85;
  }
  .vine--left { left: 0; top: 10px; width: 90px; height: 650px; }
  .vine--right { left: 805px; top: 0; width: 90px; height: 440px; }
  .brand {
    position: absolute; left: 0; right: 0; top: 185px;
    display: flex; justify-content: center; align-items: center; gap: 10px;
  }
  .brand__mark { width: 42px; height: 42px; background: var(--brand-green); }
  .brand__text { display: flex; flex-direction: column; line-height: 1; color: var(--brand-green); font-weight: 700; }
  .brand__name { font-size: 38px; letter-spacing: 2px; }
  .brand__sub { font-size: 13px; letter-spacing: 0.5px; margin-top: 4px; }
  .product-title {
    position: absolute; left: 120px; right: 150px; top: 300px;
    text-align: center;
    font-weight: 800; font-size: 80px; line-height: 1.45;
    text-transform: uppercase;
    white-space: nowrap;
    background: linear-gradient(90deg, var(--title-brown-light), var(--title-brown-dark));
    -webkit-background-clip: text; background-clip: text;
    color: transparent;
  }
  .seed-visual {
    position: absolute; left: 285px; top: 640px;
    width: 330px; height: 310px;
    border-radius: 50%;
    background: radial-gradient(circle at 45% 45%, var(--seed-light), var(--seed-dark) 75%);
  }
  .description {
    position: absolute; left: 190px; width: 550px; top: 985px;
    text-align: center; font-size: 21px; line-height: 1.35;
    color: var(--body-grey);
  }
  .wrap-tab {
    position: absolute; right: 0; top: 955px; width: 14px; height: 150px;
    background: var(--vine-green);
  }
</style>
</head>
<body>
  <main class="label">
    <svg class="label__bands" viewBox="0 0 928 1160" preserveAspectRatio="none" aria-hidden="true">
      <defs>
        <linearGradient id="bandGradient" x1="0" x2="1" y1="0" y2="0">
          <stop offset="0" stop-color="var(--band-brown)"/>
          <stop offset="0.5" stop-color="var(--band-brown-light)"/>
          <stop offset="1" stop-color="var(--band-brown)"/>
        </linearGradient>
      </defs>
      <path d="M0 0 H928 V58 C700 70 500 10 300 12 C180 13 80 20 0 30 Z" fill="url(#bandGradient)"/>
      <path d="M0 0 H928 V46 C700 56 500 0 300 2 C180 3 80 8 0 18 Z" fill="var(--label-white)"/>
      <path d="M0 1085 C120 1050 260 1060 420 1100 C600 1140 780 1120 928 1100 V1160 H0 Z" fill="url(#bandGradient)"/>
      <path d="M0 1115 C140 1080 280 1095 440 1125 C620 1160 800 1145 928 1130 V1160 H0 Z" fill="var(--label-white)"/>
    </svg>

    <div class="vine vine--left" role="img" aria-label="Climbing green ivy vine along the left edge"></div>
    <div class="vine vine--right" role="img" aria-label="Hanging green ivy vine at the top right"></div>

    <div class="brand">
      <span class="brand__mark"></span>
      <span class="brand__text">
        <span class="brand__name">VELDOR</span>
        <span class="brand__sub">BIOTECH LIMITED</span>
      </span>
    </div>

    <h1 class="product-title">Tamrel Vine<br>Kernel</h1>

    <div class="seed-visual" role="img" aria-label="Photo of cracked brown seed kernels"></div>

    <p class="description">Lorem ipsum dolor sit amet, consectetur adipisc-ing elit. Ut mollis lobortis tempus. Donec lobortis</p>

    <div class="wrap-tab"></div>
  </main>
</body>
</html>
```